Lanterns Beyond the Gate Book Cover

Looking for an inspirational cover for a Christian book called Lanterns Beyond the Gate - Mending the Weariness of the Heart & Spirit. This book features the real life stories of Delphine Orvall, a woman on a mission to spread the word of God to homeless people. The finished book will be 6" X 9", but the final page count is not known at this time. The cover should exude goodness and hope. Was thinking that the 1st "t" in the word "gate" could be made to look like a cross to create a stronger connection to the aspect of Christianity.

```html
<!DOCTYPE html>
<html lang="en">
<head>
<meta charset="utf-8">
<title>Lanterns Beyond the Gate — Book Cover</title>
<link href="https://fonts.googleapis.com/css2?family=Dancing+Script:wght@500;600&family=Quicksand:wght@300&display=swap" rel="stylesheet">
<style>
  :root {
    --stage: #f6f6f6;
    --cover-light: #e4e2df;
    --cover-mid: #d3d0cc;
    --cover-edge: #c6c3bf;
    --ink: #2f3032;
    --ink-soft: #4a4b4d;
    --art-light: #ecebe8;
    --art-dark: #bdbab6;
  }
  * { margin: 0; padding: 0; box-sizing: border-box; }
  html, body {
    width: 1200px;
    height: 800px;
    overflow: hidden;
    background: var(--stage);
  }
  .canvas {
    width: 1200px;
    height: 800px;
    display: flex;
    align-items: center;
    justify-content: center;
  }
  .cover {
    position: relative;
    width: 480px;
    height: 720px;
    background: linear-gradient(160deg, var(--cover-light) 0%, var(--cover-mid) 55%, var(--cover-edge) 100%);
    color: var(--ink);
    text-align: center;
  }
  .title {
    position: absolute;
    top: 38px;
    left: 0;
    right: 0;
    font-family: "Dancing Script", cursive;
    font-weight: 600;
    line-height: 1;
  }
  .title-main {
    display: block;
    font-size: 76px;
    letter-spacing: 1px;
  }
  .title-sub {
    display: block;
    margin-top: 2px;
    font-size: 34px;
    font-weight: 500;
  }
  .portrait {
    position: absolute;
    top: 178px;
    left: 140px;
    width: 200px;
    height: 250px;
  }
  .subtitle {
    position: absolute;
    top: 468px;
    left: 0;
    right: 0;
    font-family: "Dancing Script", cursive;
    font-weight: 600;
    font-size: 40px;
    line-height: 1.05;
    color: var(--ink);
  }
  .author {
    position: absolute;
    bottom: 34px;
    left: 0;
    right: 0;
    font-family: "Quicksand", sans-serif;
    font-weight: 300;
    font-size: 19px;
    color: var(--ink-soft);
  }
</style>
</head>
<body>
  <main class="canvas">
    <section class="cover">
      <h1 class="title">
        <span class="title-main">Lanterns</span>
        <span class="title-sub">Beyond the Gate</span>
      </h1>

      <svg class="portrait" viewBox="0 0 200 250" role="img" aria-label="Ink line drawing of a woman in a bonnet, seen in profile, holding a small red and blue flower">
        <defs>
          <radialGradient id="portraitTone" cx="50%" cy="45%" r="60%">
            <stop offset="0%" stop-color="var(--art-light)"/>
            <stop offset="100%" stop-color="var(--art-dark)"/>
          </radialGradient>
        </defs>
        <rect width="200" height="250" rx="6" fill="url(#portraitTone)"/>
      </svg>

      <p class="subtitle">Mending the Weariness<br>of the Heart &amp; Spirit</p>

      <p class="author">Name of the author</p>
    </section>
  </main>
</body>
</html>
```